Dalvor Inc Business Card

Looking to get an updated business card for a Contract Machining company (www.dalvorinc-example.com) - looking for a clean design the portrays the technical nature of the business - colors can follow the website design and be in any combination that makes sense (red black, white, metallic or silver) - logos attached for use also. Would like space for: Name, title, business phone (555 214-3098), cell phone , website (www.dalvorinc-example.com) - possibly QR code could be integrated for website (designer choice), business address - 418 Birchfield Lane, Halden Falls, OH 45099 (cards will be for 4 employees, I will either need to modify a template or I can provide individual information)
Target Market(s)
Aerospace, defense and medical device manufacturing companies that need machining
Industry/Entity Type
Machining for aerospace, defense, medical
Contact Information for Business Card
Name, Title, Business Phone, Cell Phone, email, business website and business address

```html
<!DOCTYPE html>
<html lang="en">
<head>
<meta charset="utf-8">
<title>Dalvor Inc Business Card</title>
<link href="https://fonts.googleapis.com/css2?family=Arimo:wght@400;700&display=swap" rel="stylesheet">
<style>
  :root {
    --brand-red: #b01f24;
    --paper: #ffffff;
    --ink-grey: #8a8a8a;
    --curve-shadow: #9a9a9a;
    --backdrop: #3a3a3a;
  }
  * { box-sizing: border-box; margin: 0; padding: 0; }
  html, body {
    width: 1200px; height: 689px; overflow: hidden;
    background: var(--backdrop);
    font-family: "Arimo", Arial, sans-serif;
  }
  .canvas {
    position: relative; width: 1200px; height: 689px;
    display: flex; align-items: center; justify-content: center; gap: 60px;
  }
  .card {
    position: relative; width: 520px; height: 297px;
    border-radius: 16px; overflow: hidden;
    box-shadow: 0 12px 30px rgba(0,0,0,.45);
  }
  .card-front { background: var(--brand-red); }
  .card-back { background: var(--paper); }

  .brand {
    position: absolute; display: flex; flex-direction: column; align-items: center; gap: 12px;
  }
  .brand-mark { border-radius: 50%; }
  .brand-name {
    font-weight: 700; letter-spacing: 2px; white-space: nowrap;
  }
  .card-front .brand { left: 50%; top: 50%; transform: translate(-50%, -50%); }
  .card-front .brand-mark { width: 96px; height: 96px; background: var(--paper); }
  .card-front .brand-name { color: var(--paper); font-size: 28px; }

  .card-back .brand { left: 48px; top: 92px; }
  .card-back .brand-mark { width: 76px; height: 76px; background: var(--brand-red); }
  .card-back .brand-name { color: var(--brand-red); font-size: 20px; }

  .back-shape { position: absolute; inset: 0; width: 100%; height: 100%; }

  .person { position: absolute; right: 150px; top: 34px; text-align: right; }
  .person-name { color: var(--brand-red); font-size: 21px; font-weight: 700; }
  .person-title { color: var(--ink-grey); font-size: 12px; margin-top: 2px; }

  .contact {
    position: absolute; right: 18px; top: 118px; text-align: right;
    color: var(--paper); font-size: 11.5px; line-height: 16px;
  }
  .contact-address { margin-bottom: 8px; }
  .contact-line { display: flex; justify-content: flex-end; align-items: center; gap: 6px; }
  .contact-line svg { width: 10px; height: 10px; flex: none; }
</style>
</head>
<body>
<main class="canvas">
  <section class="card card-front" aria-label="Card front">
    <div class="brand">
      <div class="brand-mark"></div>
      <div class="brand-name">DALVOR INC</div>
    </div>
  </section>

  <section class="card card-back" aria-label="Card back">
    <svg class="back-shape" viewBox="0 0 520 297" preserveAspectRatio="none" aria-hidden="true">
      <path d="M446 0 Q420 200 0 268" fill="none" stroke="var(--curve-shadow)" stroke-width="7"/>
      <path d="M452 0 Q426 206 0 274 L0 297 L520 297 L520 0 Z" fill="var(--brand-red)"/>
    </svg>

    <div class="brand">
      <div class="brand-mark"></div>
      <div class="brand-name">DALVOR INC</div>
    </div>

    <div class="person">
      <div class="person-name">Ethan Marlowe</div>
      <div class="person-title">President</div>
    </div>

    <div class="contact">
      <div class="contact-address">418 Birchfield Lane<br>Halden Falls, OH 45099</div>
      <div class="contact-line">555 214-3098
        <svg viewBox="0 0 10 10"><path d="M2 1 L4 1 L4.6 3 L3.6 3.8 Q4.6 5.6 6.2 6.4 L7 5.4 L9 6 L9 8 Q5 9 1.6 5 Q1 3 2 1Z" fill="#fff"/></svg>
      </div>
      <div class="contact-line">555 380-4721
        <svg viewBox="0 0 10 10"><rect x="2.5" y="0.5" width="5" height="9" rx="1" fill="none" stroke="#fff"/></svg>
      </div>
      <div class="contact-line">info@dalvorinc-example.com
        <svg viewBox="0 0 10 10"><rect x="0.5" y="2" width="9" height="6" fill="#fff"/><path d="M0.5 2 L5 5.5 L9.5 2" fill="none" stroke="#b01f24" stroke-width="0.8"/></svg>
      </div>
      <div class="contact-line">www.dalvorinc-example.com
        <svg viewBox="0 0 10 10"><circle cx="5" cy="5" r="4.5" fill="#fff"/><path d="M0.5 5 H9.5 M5 0.5 Q2.5 5 5 9.5 M5 0.5 Q7.5 5 5 9.5" fill="none" stroke="#b01f24" stroke-width="0.7"/></svg>
      </div>
    </div>
  </section>
</main>
</body>
</html>
```